Design for a Pool Company - Car Wraps

We require a design for our new pick up wrap. We have 3 pick ups (all Kelvaro Pandels), please use our logo.
We are a pool/hot tub/spa company. This wrap would be specifically for the Kelvaro Pandels, which are our pool cleaning vehicles.
We already have one design for the SUV (attached), so we need a design for a Pick Up truck. Please be creative however use similar design/concept as the SUV wrap.

```html
<!DOCTYPE html>
<html lang="en">
<head>
<meta charset="utf-8">
<title>Harbourline Pool &amp; Spa – Pick Up Wrap</title>
<link href="https://fonts.googleapis.com/css2?family=Poppins:wght@400;500;600&display=swap" rel="stylesheet">
<style>
  :root {
    --navy: #0b2a55;
    --blue: #2f9be0;
    --sky: #8fcdf2;
    --mist: #e6eef4;
    --white: #ffffff;
    --ground: #ffffff;
  }
  html, body {
    margin: 0;
    padding: 0;
    width: 1200px;
    height: 1200px;
    overflow: hidden;
    background: var(--ground);
  }
  .canvas {
    width: 1200px;
    height: 1200px;
    display: flex;
    flex-direction: column;
    justify-content: center;
    align-items: center;
    gap: 110px;
  }
  .wrap-panel { width: 1140px; height: 380px; display: block; }
  .brand-name { font-family: "Poppins", sans-serif; font-weight: 600; fill: var(--navy); letter-spacing: 2px; }
  .brand-sub { font-family: "Poppins", sans-serif; font-weight: 500; fill: var(--navy); letter-spacing: 4px; }
  .phone { font-family: "Poppins", sans-serif; font-weight: 600; fill: var(--mist); letter-spacing: 3px; }
  .web { font-family: "Poppins", sans-serif; font-weight: 400; fill: var(--navy); letter-spacing: 1px; }
  .social { font-family: "Poppins", sans-serif; font-weight: 500; fill: var(--white); }
</style>
</head>
<body>
<main class="canvas">

  <svg class="wrap-panel wrap-option-a" viewBox="0 0 1140 380" role="img" aria-label="Pick up side wrap, option A">
    <rect class="body-panel" x="0" y="40" width="1140" height="300" rx="18" fill="var(--white)" stroke="var(--mist)" stroke-width="2"/>
    <path class="accent-stripe" d="M760 150 C880 138 1010 128 1140 122 L1140 138 C1010 146 880 156 760 168 Z" fill="var(--sky)"/>
    <path class="accent-stripe" d="M700 190 C850 168 1000 156 1140 150 L1140 170 C1000 176 850 188 700 212 Z" fill="var(--blue)"/>
    <path class="front-stripe" d="M0 240 L240 252 L240 262 L0 252 Z" fill="var(--blue)"/>
    <path class="navy-band" d="M0 270 C220 276 420 276 560 262 C680 248 760 215 900 200 C980 192 1060 188 1140 186 L1140 322 Q1140 340 1122 340 L18 340 Q0 340 0 322 Z" fill="var(--navy)"/>
    <circle class="mark-circle" cx="695" cy="230" r="92" fill="var(--blue)"/>
    <text class="brand-name" x="300" y="226" font-size="34">HARBOURLINE</text>
    <text class="brand-sub" x="302" y="254" font-size="17">POOL &amp; SPA</text>
    <text class="phone" x="300" y="318" font-size="28">555.014.2870</text>
    <text class="web" x="1120" y="112" font-size="19" text-anchor="end">www.harbourlinepoolandspa.com</text>
    <circle class="social-dot" cx="918" cy="262" r="7" fill="var(--white)"/>
    <text class="social" x="932" y="268" font-size="16">Friendloop · Chirpit</text>
  </svg>

  <svg class="wrap-panel wrap-option-b" viewBox="0 0 1140 380" role="img" aria-label="Pick up side wrap, option B">
    <rect class="body-panel" x="0" y="40" width="1140" height="300" rx="18" fill="var(--white)" stroke="var(--mist)" stroke-width="2"/>
    <path class="accent-stripe" d="M780 150 C900 138 1020 130 1140 124 L1140 140 C1020 148 900 158 780 170 Z" fill="var(--sky)"/>
    <path class="accent-stripe" d="M740 186 C870 168 1010 158 1140 152 L1140 172 C1010 178 870 190 740 208 Z" fill="var(--blue)"/>
    <path class="front-stripe" d="M0 244 L280 262 L280 272 L0 256 Z" fill="var(--blue)"/>
    <path class="sweep-light" d="M280 262 C420 266 560 244 680 209 L700 219 C580 259 430 278 280 274 Z" fill="var(--mist)"/>
    <path class="navy-band" d="M0 264 C200 278 420 278 560 252 C680 230 760 205 900 198 C980 194 1060 192 1140 190 L1140 322 Q1140 340 1122 340 L18 340 Q0 340 0 322 Z" fill="var(--navy)"/>
    <circle class="mark-circle" cx="730" cy="210" r="100" fill="var(--blue)"/>
    <text class="brand-name" x="300" y="212" font-size="36">HARBOURLINE</text>
    <text class="brand-sub" x="302" y="242" font-size="18">POOL &amp; SPA</text>
    <text class="phone" x="330" y="316" font-size="28">555.014.2870</text>
    <text class="web" x="1120" y="112" font-size="19" text-anchor="end">www.harbourlinepoolandspa.com</text>
    <circle class="social-dot" cx="918" cy="262" r="7" fill="var(--white)"/>
    <text class="social" x="932" y="268" font-size="16">Friendloop · Chirpit</text>
  </svg>

</main>
</body>
</html>
```